International oil and gas consultancy business needs a web design

Hello, I need a web design for a new oil and gas auditing consultancy business. My business undertakes contract audit assignments to review past costs of oil and gas operations (see attached Excel file for more details of the businesses services). I need the design to give the impression of a professional consultancy style of business, rather than a retail style of website. Note: this job is for LAYOUT DESIGN ONLY and not coding / development work.
The following are my key design principles:
1. BASIC DESIGN: I am after a simple and static web design. I don't want the pages busy or cluttered with too many images or detail.
2. HORIZONTAL TABS: I require a horizontal set of tabs towards the top of the screens (see Excel file) which remain in the same position on every page.
3. META TAG PLANNING: The design should allow for effective positioning of content so that key meta tag words can easily be built during the technical build stage.
4. NUMBER OF PAGES: The site will eventually have a maximum of 10 pages. Seven of the pages will reside under the tabs. Can you please present your opening submission for the first two page.
5. USE OF MY LOGO: The attached logo (JPEG file) should be used throughout the website. Please don't change the shape and colour.
6. COLOUR SCHEMES: Can you please consider any of the 3 colour schemes below:
A - dark red (to match the logo), light grey and perhaps another of your liking;
B - dark red (to match the logo), light cream and perhaps another of your liking;
C - dark red (to match the logo), white and perhaps another of your liking.
7. WORD CONTENT: I have attached an Excel file which shows the estimated word content for each page.
8. FUTURE USE OF DESIGN: I'm planning on building a Wordpress website. Can you please ensure the layout design supports this application.

Target Market(s)

oil and gas companies (small and large)

Industry/Entity Type

Oil And Gas

Font styles to use
Sans Serif

Requirements
Nice to have
• The KOL logo and business name should ideally be next to each other. Also, the logo and name should be part of the background graphics, not above it.

```html
<!DOCTYPE html>
<html lang="en">
<head>
<meta charset="utf-8">
<title>Kestrel Oil Ledger – Oil and Gas Audit Services</title>
<link rel="stylesheet" href="https://fonts.googleapis.com/css2?family=Raleway:wght@400;500;600;700&family=Arimo:wght@400;700&family=Roboto+Condensed:wght@400;700&display=swap">
<style>
:root{
  --red:#9b1c24;
  --red-dark:#7e141b;
  --ink:#555;
  --ink-soft:#777;
  --page:#e9e9e9;
  --card:#f4f4f4;
  --nav:#4a4a4a;
  --footer:#8b8b8b;
  --footer-line:#b0b0b0;
  --white:#fff;
}
*{box-sizing:border-box;margin:0;padding:0}
html,body{width:1099px;height:1200px;overflow:hidden}
body{position:relative;background:linear-gradient(160deg,#ededed 0%,#e3e3e3 50%,#ebebeb 100%);font-family:'Arimo',Arial,sans-serif;color:var(--ink)}
.abs{position:absolute}

/* header */
.header-card{left:157px;top:16px;width:773px;height:100px;background:var(--card);box-shadow:0 6px 8px -4px rgba(0,0,0,.25)}
.brand{left:22px;top:20px;color:var(--red);font-family:'Raleway',sans-serif;font-weight:700;text-align:center;display:flex;align-items:center;gap:10px}
.brand-mark{width:14px;height:14px;background:var(--red)}
.brand-name{font-size:40px;line-height:40px;letter-spacing:3px}
.brand-full{font-size:12.5px;letter-spacing:.3px;display:block;margin-top:3px}
.main-nav{left:224px;top:32px;height:32px;width:539px;background:var(--nav);display:flex;list-style:none}
.main-nav li{flex:auto;color:#eee;font-family:'Roboto Condensed',sans-serif;font-size:10px;text-transform:uppercase;text-align:center;line-height:32px;border-right:1px solid #5d5d5d;position:relative}
.main-nav li:last-child{border-right:0}
.main-nav li.active{background:#e6e6e6;color:#222}
.main-nav li.active::after{content:"";position:absolute;left:12px;right:12px;bottom:-3px;height:3px;background:var(--red)}

.tagline{left:0;width:1099px;top:148px;text-align:center;font-family:'Raleway',sans-serif;font-size:17px;color:var(--ink-soft)}
.tagline-strong{left:0;width:1099px;top:174px;text-align:center;font-family:'Raleway',sans-serif;font-weight:700;font-size:20px;color:var(--red)}

/* hero */
.hero-photo{left:0;top:229px;width:1099px;height:318px;background:linear-gradient(180deg,#5f8cc4 0%,#9dbde0 35%,#dfe8ee 62%,#d9c94a 72%,#e0cf2f 100%)}
.hero-panel{left:295px;top:229px;width:483px;height:318px;background:rgba(255,255,255,.28)}
.social{top:12px;right:8px;display:flex;gap:4px}
.social .msg{height:22px;padding:0 8px;background:#5a5a5a;color:#fff;font-size:11px;line-height:22px;display:flex;align-items:center;gap:6px}
.social .sq{width:22px;height:22px;background:#5a5a5a}
.hero-lead{left:53px;top:81px;font-family:'Raleway',sans-serif;font-size:13px;color:#444}
.audit-list{left:53px;top:118px;list-style:none}
.audit-list li{display:flex;align-items:center;height:44px;font-family:'Raleway',sans-serif;font-size:23px;color:#444}
.audit-list svg{margin-right:8px}
.audit-list b{color:var(--red);font-weight:500;margin-right:6px}
.more{margin-left:16px;background:var(--red);color:#fff;font-family:'Arimo',sans-serif;font-size:9px;padding:3px 10px;border-radius:3px}

.intro{left:170px;width:759px;top:579px;text-align:center;font-family:'Raleway',sans-serif;font-size:13px;line-height:19px;color:#666}

/* features */
.features{left:0;top:667px;width:1099px;height:340px;background:var(--white)}
.feature{top:38px;width:150px;margin-left:-75px;text-align:center}
.feature .ring{width:58px;height:58px;border-radius:50%;margin:0 auto;display:flex;align-items:center;justify-content:center;background:var(--red)}
.feature .ring.outline{background:#fff;border:1.5px solid var(--red)}
.feature h3{font-family:'Raleway',sans-serif;font-weight:600;font-size:15px;color:#5a5a5a;margin-top:26px;line-height:19px;text-transform:uppercase}
.feature p{font-size:10px;line-height:16px;color:var(--red);margin-top:12px}

/* footer */
.footer{left:0;top:1007px;width:1099px;height:193px;background:var(--footer);color:#fff}
.f-col{top:22px;font-size:10px;line-height:16px}
.f-col h4{font-family:'Raleway',sans-serif;font-weight:400;font-size:12.5px;margin-bottom:6px}
.f-nav{list-style:none;font-family:'Roboto Condensed',sans-serif;font-size:9.5px;text-transform:uppercase;line-height:16.5px}
.f-contact{display:flex;align-items:center;gap:6px;margin-top:8px}
.f-contact.mail{color:var(--red)}
.f-field{height:18px;background:#9d9d9d;border:1px solid #a8a8a8}
.btn{background:var(--red);color:#fff;font-size:9px;text-align:center;line-height:18px}
.f-rule{left:191px;top:164px;width:726px;height:1px;background:var(--footer-line)}
.f-legal{top:172px;font-size:8.5px;color:#f0f0f0}
</style>
</head>
<body>

<header class="abs header-card">
  <div class="abs brand">
    <span class="brand-mark"></span>
    <span><span class="brand-name">KOL</span><span class="brand-full">Kestrel Oil Ledger</span></span>
  </div>
  <ul class="abs main-nav">
    <li class="active">Home</li><li>About us</li><li>Services</li><li>Our partners</li><li>Approach</li><li>Whay choose us</li><li>Contact us</li>
  </ul>
</header>

<p class="abs tagline">We specialise in providing auditing services to the oil and gas industry.</p>
<p class="abs tagline-strong">THAT'S ALL WE DO!</p>

<div class="abs hero-photo" role="img" aria-label="Photo of a yellow canola field under a blue cloudy sky with an oil pump jack"></div>
<section class="abs hero-panel">
  <div class="abs social">
    <span class="msg"><svg width="11" height="8" viewBox="0 0 11 8"><rect width="11" height="8" fill="#fff"/><path d="M0 0l5.5 4.5L11 0" stroke="#5a5a5a" fill="none"/></svg>Message</span>
    <span class="sq"></span><span class="sq"></span><span class="sq"></span>
  </div>
  <p class="abs hero-lead">We are specialise in:</p>
  <ul class="abs audit-list">
    <li><svg width="10" height="14" viewBox="0 0 10 14"><path d="M5 1C3 5 1 7 1 9.5a4 4 0 008 0C9 7 7 5 5 1z" fill="none" stroke="#444" stroke-width="1.4"/></svg><b>JOINT</b>VENTURE AUDITS<span class="more">MORE</span></li>
    <li><svg width="10" height="14" viewBox="0 0 10 14"><path d="M5 1C3 5 1 7 1 9.5a4 4 0 008 0C9 7 7 5 5 1z" fill="none" stroke="#444" stroke-width="1.4"/></svg><b>CONTRACT</b>AUDITS<span class="more">MORE</span></li>
    <li><svg width="10" height="14" viewBox="0 0 10 14"><path d="M5 1C3 5 1 7 1 9.5a4 4 0 008 0C9 7 7 5 5 1z" fill="none" stroke="#444" stroke-width="1.4"/></svg><b>OPERATIONS</b>AUDITS<span class="more">MORE</span></li>
  </ul>
</section>

<p class="abs intro">Kestrel Oil Ledger is a Perth (Australia) based firm specialising in providing quality audit services for the oil and gasidustry. Our skills and knowledge of oil and gas, along with a deep understanding of business commercial needs, ensures the high quality of our services.</p>

<section class="abs features">
  <div class="abs feature" style="left:279px">
    <div class="ring outline"><svg width="16" height="18" viewBox="0 0 16 18"><rect x="2" y="1" width="12" height="16" rx="1.5" fill="none" stroke="#9b1c24" stroke-width="1.6"/><path d="M5 6h6M5 9h6M5 12h6" stroke="#9b1c24" stroke-width="1.4"/></svg></div>
    <h3>Risk mitigation</h3>
    <p>From compliance with JOA or PSC conditions to agree­ments with contractors, we have the experience to review, assess and suggest procedural improvements (incl. feedback on improve­ments to contract terms).</p>
  </div>
  <div class="abs feature" style="left:475px">
    <div class="ring"><svg width="22" height="18" viewBox="0 0 22 18"><ellipse cx="11" cy="9" rx="8" ry="6" fill="#fff"/><rect x="6" y="13" width="3" height="4" fill="#fff"/><rect x="13" y="13" width="3" height="4" fill="#fff"/><rect x="9" y="3" width="4" height="1.5" fill="#9b1c24"/></svg></div>
    <h3>Cost savings</h3>
    <p>Our experience has taught us how to quickly identify financial risk areas and then propose possible solutions</p>
  </div>
  <div class="abs feature" style="left:663px">
    <div class="ring"><svg width="20" height="18" viewBox="0 0 20 18"><path d="M2 16h16" stroke="#fff" stroke-width="1.5"/><rect x="4" y="10" width="3" height="6" fill="#fff"/><rect x="9" y="7" width="3" height="9" fill="#fff"/><rect x="14" y="4" width="3" height="12" fill="#fff"/><path d="M3 8l5-4 4 2 5-5" stroke="#fff" fill="none" stroke-width="1.2"/></svg></div>
    <h3>Process<br>improvement</h3>
    <p>Working within and reviewing world class progressive organi­sations provides us with insight into best practise oil and gas processes and procedures. We can apply this knowledge to your company and/or your business partners.</p>
  </div>
  <div class="abs feature" style="left:852px">
    <div class="ring"><svg width="16" height="18" viewBox="0 0 16 18"><rect x="1" y="1" width="14" height="16" rx="1.5" fill="none" stroke="#fff" stroke-width="1.6"/><path d="M4 6h1M7 6h5M4 9h1M7 9h5M4 12h1M7 12h5" stroke="#fff" stroke-width="1.4"/></svg></div>
    <h3>Contractual efficiency &amp; effrectiveness</h3>
    <p>Through audit and review assign­ments we can identify and report cost savings initiatives.</p>
  </div>
</section>

<footer class="abs footer">
  <div class="abs f-col" style="left:191px">
    <h4>Kestrel Oil Ledger</h4>
    <ul class="f-nav"><li>Home</li><li>About us</li><li>Services</li><li>Our partners</li><li>Approach</li><li>Whay choose us</li><li>Contact us</li></ul>
  </div>
  <div class="abs f-col" style="left:400px">
    <h4>Registered Office:</h4>
    <p>Unit 9, 12 Harbour Lane<br>Northgate WA 6000<br>Australia</p>
    <p class="f-contact" style="margin-top:20px"><svg width="11" height="11" viewBox="0 0 11 11"><path d="M2 1l2 0 1 3-1.5 1a6 6 0 002.5 2.5L7 6l3 1v2c0 1-1 1-1 1A8 8 0 011 2s0-1 1-1z" fill="#fff"/></svg>+61 (0)400 000 123</p>
    <p class="f-contact mail"><svg width="12" height="9" viewBox="0 0 12 9"><rect width="12" height="9" fill="#9b1c24"/><path d="M0 0l6 5 6-5" stroke="#8b8b8b" fill="none"/></svg>hello@kestreloil.example</p>
  </div>
  <div class="abs f-col" style="left:591px">
    <h4>Postal Address:</h4>
    <p>14 Reed Road<br>Westfield WA 6010<br>Australia</p>
  </div>
  <div class="abs f-col" style="left:735px;width:182px">
    <p style="margin-bottom:4px">For Newsletter enter your e-mail:</p>
    <div style="display:flex;gap:4px"><div class="f-field" style="width:155px"></div><div class="btn" style="width:23px">GO</div></div>
    <p style="margin:6px 0 4px">Do you have a question?</p>
    <div class="f-field" style="width:182px;height:44px"></div>
    <div class="btn" style="width:38px;margin:8px 0 0 144px">SEND</div>
  </div>
  <div class="abs f-rule"></div>
  <p class="abs f-legal" style="left:358px">Copyright © 2014</p>
  <p class="abs f-legal" style="left:497px">Terms and Conditions</p>
  <p class="abs f-legal" style="left:652px">Privacy policy</p>
</footer>

</body>
</html>
```